Vehicle Rental Hire in the Algarve - Portugal

We are opening a Vehicle Rental company in the Algarve - Portugal - this will attract both locals and Tourists visiting. So we want this website to capture the beautiful location we will be set in, along with the familiarity of a vehicle rental company. And to keep a colour scheme in Line with out Logo. We are Fenmarel Vehicle Rental.

Industry/Entity Type

Vehicle Rental

Number of Pages Required

1 page

Requirements
Must have
• must be professional, and simple to use navigation bar - must also have a "make a reservation" box - similar to the screenshot attached - Under our logo it must read "Vehicle Rental"
Nice to have
• It needs to be in a colour scheme that fits in with our logo

```html
<!DOCTYPE html>
<html lang="pt">
<head>
<meta charset="UTF-8">
<title>Fenmarel Vehicle Rental</title>
<link href="https://fonts.googleapis.com/css2?family=Figtree:wght@400;500;600;700;800&display=swap" rel="stylesheet">
<style>
:root{
  --brand-blue:#1a14e0;
  --accent-red:#e0192b;
  --white:#ffffff;
  --panel:rgba(240,241,245,0.93);
  --field:#f8f8fa;
  --ink:#1b1b2a;
  --muted:#6b6b78;
}
*{margin:0;padding:0;box-sizing:border-box}
html,body{width:1200px;height:755px;overflow:hidden}
body{font-family:'Figtree',sans-serif;background:var(--white);position:relative;color:var(--ink)}
.hero{position:absolute;left:0;top:0;width:1200px;height:600px;
  background:linear-gradient(160deg,#2b3a8a 0%,#6b5aa8 30%,#c79a7a 60%,#8a5a3c 80%,#3a2a30 100%)}
.hero-shade{position:absolute;inset:0;background:linear-gradient(90deg,rgba(20,20,60,.35),rgba(20,20,60,0) 60%)}
.brand{position:absolute;left:141px;top:36px;color:var(--white);font-weight:700;text-align:center;width:120px}
.brand-name{font-size:22px;letter-spacing:.5px}
.brand-tag{font-size:10px;font-weight:700;margin-top:4px}
.nav{position:absolute;top:39px;left:600px;height:35px;display:flex;align-items:center;gap:0}
.nav a{color:var(--white);text-decoration:none;font-size:13px;font-weight:400;position:absolute;white-space:nowrap}
.nav a.active{color:var(--accent-red)}
.nav .cta{background:var(--brand-blue);border-radius:18px;height:35px;width:127px;display:flex;align-items:center;justify-content:center}
.headline{position:absolute;left:141px;top:158px;color:var(--white);font-size:41px;font-weight:800;line-height:50px;letter-spacing:.2px}
.sub{position:absolute;left:141px;color:var(--white);font-weight:500}
.sub-1{top:321px;font-size:22px}
.sub-2{top:363px;font-size:28px;text-decoration:underline;text-underline-offset:5px;text-decoration-thickness:2px}
.sub-3{top:414px;font-size:22px}
.booking{position:absolute;left:771px;top:115px;width:274px;height:446px;background:var(--panel)}
.tabs{display:flex;height:35px}
.tab{flex:1;display:flex;align-items:center;justify-content:center;font-size:12.5px;font-weight:500}
.tab-active{background:var(--brand-blue);color:var(--white)}
.tab-idle{background:var(--white);color:var(--brand-blue)}
.field{position:absolute;left:14px;width:246px;height:44px;background:var(--field);display:flex;align-items:center;padding-left:10px;gap:8px}
.field svg{flex:none}
.label{font-size:9.5px;font-weight:600;color:var(--ink)}
.value{font-size:12.5px;color:var(--muted);margin-top:1px}
.consent{position:absolute;left:14px;top:347px;display:flex;gap:7px;font-size:9.5px;line-height:13.5px;color:var(--ink)}
.consent .box{width:11px;height:11px;background:#e3e4ea;flex:none;margin-top:1px}
.reserve{position:absolute;left:66px;top:388px;width:141px;height:35px;border-radius:18px;background:var(--brand-blue);color:var(--white);font-size:12.5px;display:flex;align-items:center;justify-content:center}
.support-band{position:absolute;left:0;top:600px;width:1200px;height:117px;background:var(--brand-blue)}
.agent{position:absolute;left:141px;top:583px;width:186px;height:134px;background:linear-gradient(180deg,#3a3550,#d9dbe3);border-radius:60px 60px 0 0}
.support{position:absolute;left:340px;top:630px;color:var(--white)}
.support h2,.newsletter h2{font-size:18px;font-weight:700}
.phone{display:flex;align-items:center;gap:6px;font-size:25px;font-weight:700;margin-top:4px}
.newsletter{position:absolute;left:758px;top:630px;color:var(--white)}
.email{margin-top:4px;width:301px;height:35px;border:1px solid var(--white);display:flex;align-items:center;justify-content:space-between;padding:0 10px;font-size:14px;font-weight:500}
.footer{position:absolute;left:0;top:717px;width:1200px;height:38px;display:flex;align-items:center;justify-content:center;font-size:13px;color:var(--ink)}
</style>
</head>
<body>
<section class="hero" role="img" aria-label="Photo of a black luxury car with a chauffeur on a lit historic city street at dusk">
  <div class="hero-shade"></div>
</section>

<div class="brand">
  <div class="brand-name">Fenmarel</div>
  <div class="brand-tag">Vehicle Rental</div>
</div>

<nav class="nav">
  <a class="active" href="#" style="left:33px">Início</a>
  <a href="#" style="left:81px">Frota</a>
  <a href="#" style="left:147px">Sobre Nós</a>
  <a href="#" style="left:244px">Parceiros</a>
  <a class="cta" href="#" style="left:332px;top:-17px">Contactar-Nos</a>
</nav>

<h1 class="headline">Aluguer De Automóveis<br>No Aeroporto De Faro -<br>Não Há Queixas Connosco!</h1>
<p class="sub sub-1">Reserve Agora Ou Contacte-nos</p>
<p class="sub sub-2">Obtenha O Melhor Negócio!</p>
<p class="sub sub-3">Aeroporto De Faro, RESERVE JÁ!</p>

<form class="booking">
  <div class="tabs">
    <div class="tab tab-active">Na One Direction</div>
    <div class="tab tab-idle">Na Hora</div>
  </div>
  <div class="field" style="top:56px">
    <svg width="16" height="18" viewBox="0 0 16 18" fill="none" stroke="#1a14e0" stroke-width="1.3"><path d="M8 17s6-5.5 6-10A6 6 0 0 0 2 7c0 4.5 6 10 6 10z"/><circle cx="8" cy="7" r="2.2"/></svg>
    <div><div class="label">Onde</div><div class="value">Endereço, aeroporto, hotel...</div></div>
  </div>
  <div class="field" style="top:113px">
    <svg width="17" height="17" viewBox="0 0 17 17" fill="none" stroke="#1a14e0" stroke-width="1.3"><rect x="1" y="3" width="15" height="13" rx="1.5"/><path d="M1 7h15M5 1v4M12 1v4"/><path d="M4 10h1M8 10h1M12 10h1M4 13h1M8 13h1M12 13h1"/></svg>
    <div><div class="label">Data</div><div class="value">23/04/2024</div></div>
  </div>
  <div class="field" style="top:170px">
    <svg width="17" height="17" viewBox="0 0 17 17" fill="none" stroke="#1a14e0" stroke-width="1.3"><circle cx="8.5" cy="8.5" r="7.5"/><path d="M8.5 4v4.5L6 11"/></svg>
    <div><div class="label">Tempo</div><div class="value">20 ⌄ :45 ⌄</div></div>
  </div>
  <div class="field" style="top:228px">
    <svg width="18" height="16" viewBox="0 0 18 16" fill="none" stroke="#1a14e0" stroke-width="1.3"><circle cx="6" cy="5" r="3"/><path d="M1 15c0-3 2.2-5 5-5s5 2 5 5"/><circle cx="13" cy="5" r="2.3"/><path d="M12 10c3 0 5 1.8 5 5"/></svg>
    <div><div class="label">Passageiros</div><div class="value">02 ⌄</div></div>
  </div>
  <div class="field" style="top:291px">
    <svg width="14" height="20" viewBox="0 0 14 20" fill="none" stroke="#1a14e0" stroke-width="1.3"><rect x="1.5" y="5" width="11" height="13" rx="1.5"/><path d="M5 5V1.5h4V5M5 8v7M9 8v7M4 18v1.5M10 18v1.5"/></svg>
    <div><div class="label">Bagagem</div><div class="value">04 ⌄</div></div>
  </div>
  <div class="consent">
    <span class="box"></span>
    <span>Aceito receber comunicações por correio<br>eletrónico relativas ao meu pedido de orçamento.</span>
  </div>
  <div class="reserve">Reservar Agora</div>
</form>

<section class="support-band"></section>
<div class="agent" role="img" aria-label="Illustration of a customer support agent with headset at a laptop"></div>
<div class="support">
  <h2>Apoio Ao Cliente</h2>
  <div class="phone">
    <svg width="18" height="18" viewBox="0 0 24 24" fill="#ffffff"><path d="M6.6 10.8a15.1 15.1 0 0 0 6.6 6.6l2.2-2.2c.3-.3.7-.4 1-.2 1.1.4 2.3.6 3.6.6.6 0 1 .4 1 1V20c0 .6-.4 1-1 1A17 17 0 0 1 3 4c0-.6.4-1 1-1h3.5c.6 0 1 .4 1 1 0 1.3.2 2.5.6 3.6.1.3 0 .7-.2 1z"/></svg>
    <span>123-456-7890</span>
  </div>
</div>
<div class="newsletter">
  <h2>Subscrever A Newsletter</h2>
  <div class="email">
    <span>Introduza O Seu E-mail</span>
    <svg width="20" height="20" viewBox="0 0 24 24" fill="#ffffff"><path d="M2 11 22 2l-6 20-4-8-10-3zm10 3 2 4 4-13-6 9z"/></svg>
  </div>
</div>

<footer class="footer">© 2024 Fenmarel. Todos Os Direitos Reservados.</footer>
</body>
</html>
```